Label for Skincare Brand

"Fernbrook Organics" - organic skincare brand
I need a label designed for my organic skincare brand. I have attached pics of brands I like, to give you an idea of style. I would like something minimal although some colour might work. Colours I like are pale blush pink and aqua. I would like a clean, minimalistic modern yet elegant label. Please look at the samples because they demonstrate the style I look for in a label. It is okay to add a graphical element into the design as long as it enhances or add value to the design.
We do not have a logo yet, so I'd appreciate if you could create a simple type logo for Fernbrook Organics similar to the examples attached.
Please can you do two different sizes: one cream jar and one serum bottle. Both will contain the same information.
___________________________________________________
1. Cream Jar (label size 42 x 190 mm) (clear glass with aluminium lid)
2. Serum Bottle (label size 50 x 110 mm) (clear glass with black pump)
FRONT SIDE:
Fernbrook Organics
Moonpetal
Ultimate Anti-Aging Cream
For Dry & Mature Skin
Organic & Palm Oil-Free
100 ml.
BACK SIDE:
Moonpetal Radiance Renewal Cream
An effective Day Cream that harnesses the best of science to target the signs of aging. The main active ingredient is K7M, a patented noncomedogenic lipid complex, carefully engineered from botanically-sourced lipids. It is composed of a variety of lipid types which are carefully combined in the same ratio as those found on healthy young skin of an average Moonpetal year old.
Directions:
Apply to clean skin morning and night.
Ingredients:
Aloe Vera Leaf Juice, Cocos Nucifera Oil, Butyrospermum Parkii Butter, Jojoba Oil/Macadamia Seed Oil Esters (and) Squalene (and) Phytosteryl Macadamiate (and) Phytosterols, Potassium Olivoyl Hydrolyzed Oat Protein (and) Cetearyl Alcohol (and) Glyceryl Oleate (and) Glyceryl Stearat, Benzyl Alcohol, Dehydroacetic Acid.
Fernbrook Organics
3/6 Kellerton Parade West, Wahroonga, NSW 2076
www.fernbrookorganics.example
Any questions, please just ask away. Thank you.

```html
<!DOCTYPE html>
<html lang="en">
<head>
<meta charset="utf-8">
<title>Fernbrook Organics – Moonpetal Cream Jar Label</title>
<link rel="stylesheet" href="https://fonts.googleapis.com/css2?family=Montserrat:wght@300;400;500;600&display=swap">
<style>
  :root {
    --canvas: #ffffff;
    --label-white: #ffffff;
    --ink: #111111;
    --badge-grey: #a9a9a9;
    --blush-deep: #b88fb4;
    --blush-mid: #d5acd3;
    --blush-light: #ebc5ea;
    --label-shadow: rgba(0, 0, 0, 0.18);
  }
  * { box-sizing: border-box; margin: 0; padding: 0; }
  html, body {
    width: 1000px;
    height: 1200px;
    overflow: hidden;
    background: var(--canvas);
    font-family: "Montserrat", Arial, sans-serif;
    color: var(--ink);
  }
  .jar-label {
    position: absolute;
    left: 130px;
    top: 427px;
    width: 740px;
    height: 346px;
    background: var(--label-white);
    box-shadow: 0 2px 10px var(--label-shadow);
  }
  .label-header {
    position: relative;
    height: 123px;
  }
  .brand-name {
    position: absolute;
    left: 0;
    right: 0;
    top: 62px;
    text-align: center;
    font-weight: 400;
    font-size: 16px;
    line-height: 1;
    letter-spacing: 0.02em;
    text-transform: uppercase;
  }
  .organic-badge {
    position: absolute;
    left: 553px;
    top: 16px;
  }
  .label-band {
    position: relative;
    height: 223px;
    background: linear-gradient(90deg,
      var(--blush-deep) 0%, var(--blush-mid) 14%, var(--blush-light) 26%,
      var(--blush-mid) 40%, var(--blush-light) 52%, var(--blush-mid) 64%,
      var(--blush-light) 76%, var(--blush-mid) 88%, var(--blush-deep) 100%);
  }
  .product-title {
    position: absolute;
    left: 0;
    right: 0;
    top: 50px;
    display: flex;
    justify-content: center;
    align-items: center;
    gap: 22px;
  }
  .product-name {
    font-weight: 400;
    font-size: 62px;
    line-height: 1;
    letter-spacing: -0.01em;
  }
  .product-claims {
    display: flex;
    flex-direction: column;
    gap: 9px;
  }
  .claim-range {
    font-weight: 600;
    font-size: 32px;
    line-height: 1;
    letter-spacing: 0.5em;
  }
  .claim-type {
    font-weight: 500;
    font-size: 19px;
    line-height: 1;
    letter-spacing: 0.2em;
  }
  .claim-skin {
    font-weight: 600;
    font-size: 13px;
    line-height: 1;
    letter-spacing: 0.34em;
  }
  .product-volume {
    position: absolute;
    left: 0;
    right: 0;
    bottom: 16px;
    text-align: center;
    font-weight: 400;
    font-size: 18px;
  }
</style>
</head>
<body>
  <section class="jar-label">
    <header class="label-header">
      <span class="brand-name">Fernbrook Organics</span>
      <svg class="organic-badge" width="96" height="96" viewBox="0 0 96 96" role="img" aria-label="Organic and palm oil free badge">
        <circle cx="48" cy="48" r="45" fill="none" stroke="var(--badge-grey)" stroke-width="2"/>
        <circle cx="48" cy="48" r="24" fill="none" stroke="var(--badge-grey)" stroke-width="1.5"/>
      </svg>
    </header>
    <div class="label-band">
      <div class="product-title">
        <span class="product-name">Moonpetal</span>
        <div class="product-claims">
          <span class="claim-range">ULTIMATE</span>
          <span class="claim-type">ANTI-AGEING CREAM</span>
          <span class="claim-skin">FOR DRY &amp; MATURE SKIN</span>
        </div>
      </div>
      <p class="product-volume">100 ml</p>
    </div>
  </section>
</body>
</html>
```